Tobin's Harbor Table Restaurant and Bar

Tobin's Harbor Table is a casual dining restaurant and bar experience. We are owned by Gregory (originally from Lakeport), and Lorna (originally from Red Mesa, Sonora Valley). Gregory and Lorna spent much of their lives traveling and working around the world and have landed in Las Brisas, Cerro Alto, Republic of Marenta, where they own Tobin's Harbor Table, a popular, casual dining restaurant and watering hole. Tobin's has been here for over four years, and is in desperate need of a website makeover.

Our website should be easy to maintain, clean look and represent our brand, and our logo. We need to easily maintain the content as we have constant new events, holidays, sponsorships, sports, live music, etc.

We live in the agricultural hub of Central American, and we dedicated to all our ingredients being local, however, used in dishes that represent all corners of the globe. Some of our favorites are our Orange Chicken, Pad Thai, North Carolina Pulled Pork.

We also have the largest beer selection in all of panama with three local microbrews and beers and wines from every corner of the globe, ncluding a growing collection of American Microbrews . . . We also have the best whiskey selection including American, Irish, Scottish, Canadian, randing from $2 to $50 a shot . . .

We take pride in great food in a "divey" atmosphere . . .

www.tobinsharbortable.example
Las Brisas, Cerro Alto, Republic of Marenta

Also, We want the website to direct to another website for special events and such, something easy to maintain or that is imbedded into site, we want the site to be static, but current, where social media will serve as a way to discuss what changes day-to-day more than the website.
Updates

Our webpage is a good reference, but hard and cumbersome to update, make it easy and simple, clean and modern looking. Check our facebook page at Tobin's Harbor Table in Boquete for more up-to-date information. Greg

Target Market(s)

Tourists, Panamanian Customers, Expatriates, and other Locals. Sports and Live Music fans.

Industry/Entity Type

Restaurant

Number of Pages Required

1 page

Font styles to use
Other font styles liked:
• Please see our logo, and compliment or parallel as appropriate

Requirements
Must have
• Links to my menus or menus easily embedded into the site, I can provide links or pdf or jpg files of menus.
Nice to have
• Ability to switch between a Spanish and English version (I can have the website translated, but there should be two sides of the site, links to voyagerate, and social media.

```html
<!DOCTYPE html>
<html lang="en">
<head>
<meta charset="utf-8">
<title>Tobin's Harbor Table Restaurant and Bar</title>
<link rel="stylesheet" href="https://fonts.googleapis.com/css2?family=Raleway:wght@400;500;600&family=Open+Sans:wght@400;600&display=swap">
<style>
:root{
  --green:#5f9130;
  --green-dark:#4a7a22;
  --green-light:#76a83f;
  --text:#333333;
  --muted:#5a5a5a;
  --brown:rgba(84,58,28,.88);
  --teal:#3d8782;
  --teal-dark:#2f6f6c;
  --footer:#f3f3f3;
  --white:#ffffff;
}
*{box-sizing:border-box;margin:0;padding:0}
html,body{width:858px;height:1200px;overflow:hidden;background:var(--white)}
body{font-family:"Open Sans",Arial,sans-serif;color:var(--text);position:relative}
.abs{position:absolute}

/* header */
.brand{left:135px;top:24px;display:flex;align-items:center;gap:8px}
.brand-mark{width:34px;height:34px;border-radius:50%;background:var(--green)}
.brand-name{font-family:"Raleway",sans-serif;font-weight:600;font-size:16px;color:var(--green-dark);line-height:1.05}
.brand-place{left:135px;top:67px;font-family:"Open Sans",sans-serif;font-size:5.5px;font-weight:600;color:#3d2b16;letter-spacing:.2px;white-space:nowrap}
.lang{left:654px;top:21px;width:65px;height:18px;border:1px solid #cfcfcf;font-size:8px;display:flex;align-items:center;gap:5px;padding-left:7px;color:#333}
.lang-flag{width:12px;height:8px;background:#2b3f7f;border:1px solid #c9c9c9}
.lang-caret{width:0;height:0;border-left:3px solid transparent;border-right:3px solid transparent;border-top:4px solid #666;margin-left:2px}
.social{top:51px;display:flex;gap:4px;left:626px}
.social span{width:20px;height:20px;border-radius:50%;background:var(--green)}

/* nav */
.nav{left:0;top:87px;width:858px;height:37px;background:linear-gradient(var(--green-light),var(--green-dark));display:flex;justify-content:center}
.nav ul{list-style:none;display:flex;margin-left:-16px}
.nav li{color:var(--white);font-family:"Raleway",sans-serif;font-size:10.5px;font-weight:500;line-height:37px;padding:0 22px;border-left:1px solid rgba(255,255,255,.25)}
.nav li:first-child{border-left:none}

/* hero */
.hero{left:0;top:124px;width:858px;height:331px;background:linear-gradient(100deg,#5a3a26 0%,#8a5a35 30%,#6b4a30 55%,#9a6b40 80%,#4b3222 100%)}
.hero-caption{left:133px;top:232px;width:310px;height:118px;background:var(--brown);padding:17px 22px;color:var(--white)}
.hero-title{font-family:"Raleway",sans-serif;font-weight:400;font-size:23px;line-height:26px}
.hero-sub{font-family:"Raleway",sans-serif;font-size:19px;line-height:22px}
.hero-text{font-size:7px;line-height:11px;margin-top:8px;color:#e9ded0}
.dots{left:399px;top:427px;display:flex;gap:2px}
.dots span{width:14px;height:14px;border-radius:50%;background:var(--white)}
.dots span.active{background:#111}

/* about */
.about{left:0;top:490px;width:858px;text-align:center}
.about h2{font-family:"Raleway",sans-serif;font-weight:400;font-size:20px;color:#222;margin-bottom:10px}
.about p{font-size:7px;line-height:12.8px;color:var(--muted);width:560px;margin:0 auto 5px}
.about-shade{left:140px;top:612px;width:578px;height:30px;background:radial-gradient(ellipse at 50% 100%,rgba(0,0,0,.08),transparent 70%)}

/* features */
.features{left:0;top:649px;width:858px;height:252px;background:linear-gradient(90deg,var(--teal-dark),var(--teal) 50%,var(--teal-dark))}
.feature{top:693px;width:130px;text-align:center;color:var(--white)}
.feature svg{display:block;margin:0 auto;height:56px}
.feature h3{font-family:"Raleway",sans-serif;font-weight:400;font-size:14px;margin-top:18px}
.feature p{font-size:7px;line-height:11.2px;margin-top:4px;color:#e7f1f0}
.feature .btn{display:inline-block;margin-top:10px;width:64px;height:21px;border:2px solid var(--white);font-size:7.5px;line-height:17px}

/* events */
.events-title{left:132px;top:939px;font-family:"Raleway",sans-serif;font-weight:400;font-size:17px;color:#222}
.event-photo{top:977px;width:120px;height:84px}
.event-body{top:976px;width:160px}
.event-body h4{font-family:"Raleway",sans-serif;font-weight:500;font-size:9.5px;color:var(--green)}
.event-body p{font-size:7px;line-height:12.8px;color:var(--muted);margin-top:3px}
.event-body a{display:block;font-size:9px;color:#333;margin-top:6px;text-decoration:none}

/* footer */
.footer{left:0;top:1117px;width:858px;height:83px;background:var(--footer);border-top:1px solid #dcdcdc}
.footer-nav{left:135px;top:1142px;display:flex;gap:24px;font-size:10px;color:#333;list-style:none}
.copyright{left:135px;top:1164px;font-size:7px;color:#555}
.review{left:595px;top:1140px;display:flex;align-items:center;gap:6px}
.review-mark{width:20px;height:20px;border-radius:50%;background:#222}
.review-name{font-family:"Open Sans",sans-serif;font-size:17px;color:#222}
</style>
</head>
<body>

<header>
  <div class="abs brand"><span class="brand-mark"></span><span class="brand-name">Tobin's<br>Harbor Table</span></div>
  <div class="abs brand-place">LAS BRISAS, CERRO ALTO, REPUBLIC OF MARENTA</div>
  <div class="abs lang"><span class="lang-flag"></span>English<span class="lang-caret"></span></div>
  <div class="abs social" aria-label="Social links"><span></span><span></span><span></span><span></span></div>
</header>

<nav class="abs nav">
  <ul>
    <li>HOME</li><li>ABOUT US</li><li>FIND US</li><li>MENU</li><li>GALLERY</li><li>EVENTS</li><li>CONTACT US</li>
  </ul>
</nav>

<section>
  <div class="abs hero" role="img" aria-label="Two women smiling and dining at a restaurant table with plates of food and drinks"></div>
  <div class="abs hero-caption">
    <h1 class="hero-title">Casual Dining Restaurant</h1>
    <div class="hero-sub">and Bar Experience</div>
    <p class="hero-text">Class aptent taciti sociosqu ad litora torquent per conubia nostra per inceptos hymenaeos Proin nulla arcu nonummy luctus dictu</p>
  </div>
  <div class="abs dots"><span class="active"></span><span></span><span></span><span></span></div>
</section>

<section class="abs about">
  <h2>ABOUT OUR COMPANY</h2>
  <p>Tobin's Harbor Table is a casual dining restaurant and bar experience. We are owned by Gregory (originally from Lakeport), and Lorna (originally from Red Mesa, Sonora Valley). Gregory and Lorna spent much of their lives traveling and working around the world and have landed in Las Brisas, Cerro Alto, Republic of Marenta, where they own Tobin's Harbor Table, a popular, casual dining restaurant and watering hole.</p>
  <p>Tobin's has been here for over four years, and is in desperate need of a website makeover. Our website should be easy to maintain, clean look and represent our brand, and our logo. We need to easily maintain the content as we have constant new events, holidays, sponsorships, sports, live music, etc.</p>
</section>
<div class="abs about-shade"></div>

<section>
  <div class="abs features" role="img" aria-label="Friends cheering and raising drinks at a bar, tinted teal"></div>

  <div class="abs feature" style="left:131px">
    <svg viewBox="0 0 60 56" fill="none" stroke="#fff" stroke-width="3">
      <path d="M8 36h44"/><path d="M12 36l5 14h6l5-14M26 36l5 14h6l5-14" stroke-width="2.5"/>
      <circle cx="34" cy="10" r="4" fill="#fff" stroke="none"/><path d="M34 15v14M28 20h12M22 6v28"/>
    </svg>
    <h3>Live Music</h3>
    <p>Class aptent taciti sociosqu ad litora torquent per conubia nostra per inceptos hymenaeos</p>
    <span class="btn">View More</span>
  </div>

  <div class="abs feature" style="left:278px">
    <svg viewBox="0 0 60 56" fill="#fff">
      <path d="M22 24l14 6-10 24z"/>
      <path d="M40 4l2 5 5 1-4 3 1 5-4-3-4 3 1-5-4-3 5-1z"/><path d="M24 2l1.5 4 4 .5-3 2.5 1 4-3.5-2-3.5 2 1-4-3-2.5 4-.5z"/>
      <circle cx="50" cy="22" r="2"/><circle cx="14" cy="14" r="2"/><circle cx="32" cy="16" r="1.6"/>
    </svg>
    <h3>Event &amp; Holidays</h3>
    <p>Class aptent taciti sociosqu ad litora torquent per conubia nostra per inceptos hymenaeos</p>
    <span class="btn">View More</span>
  </div>

  <div class="abs feature" style="left:430px">
    <svg viewBox="0 0 60 56" fill="#fff">
      <circle cx="28" cy="8" r="3"/><path d="M8 32a20 20 0 0 1 40 0z"/><rect x="4" y="34" width="48" height="4" rx="2"/>
      <path d="M30 42h22v6H34z"/>
    </svg>
    <h3>Food &amp; Beer</h3>
    <p>Class aptent taciti sociosqu ad litora torquent per conubia nostra per inceptos hymenaeos</p>
    <span class="btn">View More</span>
  </div>

  <div class="abs feature" style="left:582px">
    <svg viewBox="0 0 60 56" fill="none" stroke="#fff" stroke-width="3">
      <ellipse cx="30" cy="28" rx="24" ry="14" transform="rotate(-40 30 28)"/>
      <path d="M22 36l16-16M26 26l4 4M30 22l4 4M34 18l4 4" stroke-width="2.5"/>
    </svg>
    <h3>Sports</h3>
    <p>Class aptent taciti sociosqu ad litora torquent per conubia nostra per inceptos hymenaeos</p>
    <span class="btn">View More</span>
  </div>
</section>

<section>
  <h2 class="abs events-title">Latest Events</h2>
  <div class="abs event-photo" style="left:133px;background:linear-gradient(135deg,#3a2410,#a9702e 50%,#2a180a)" role="img" aria-label="Chef serving guests at a candlelit dinner table"></div>
  <div class="abs event-body" style="left:266px">
    <h4>Morbi diam mauris viverra</h4>
    <p>Morbi eget arcu Morbi porta libero id ullamcorper nonummy nibh ligula pulvinar metus eget consectetuer augue nisi quis lacus Ut ac mi quis lacus mollis aliquam</p>
    <a>Read More</a>
  </div>
  <div class="abs event-photo" style="left:440px;background:linear-gradient(135deg,#1d2a4a,#5a4d6e 45%,#1a7a7a)" role="img" aria-label="Woman holding a cocktail in a lively bar"></div>
  <div class="abs event-body" style="left:573px">
    <h4>Sed metus augue convallis et</h4>
    <p>Morbi eget arcu Morbi porta libero id ullamcorper nonummy nibh ligula pulvinar metus eget consectetuer augue nisi quis lacus Ut ac mi quis lacus mollis aliquam</p>
    <a>Read More</a>
  </div>
</section>

<footer>
  <div class="abs footer"></div>
  <ul class="abs footer-nav"><li>Home</li><li>About Us</li><li>Event</li><li>Menu</li><li>Blog</li><li>Contact</li></ul>
  <div class="abs copyright">© 2015 Company Name &nbsp;All right reserved &nbsp;Term of Use</div>
  <div class="abs review"><span class="review-mark"></span><span class="review-name">voyagerate</span></div>
</footer>

</body>
</html>
```